Visual consulting framework

Thornwell Advisory is a financial consulting business that takes it clients on the following journey:
1. Get fit (disciplined)
2. Get funded (access to capital)
3. Get big (grow)
4. Get out (exit with wealth)
Over thirty years we have identified that the key to being successful on this journey are the following elements or components.
1. Vision
2. Strategy
3. Structure
4. Product & services
5. Sales and marketing
6. System and processes
7. People
8. Culture
9. Finance
10. M&A
11. Performance monitoring
12. Risk management
We require a visual representation of these elements and the journey to communicate to clients and prospects in marketing material.
Look and feel
Each slider illustrates characteristics of the customer's brand and the style your logo design should communicate.

```html
<!DOCTYPE html>
<html lang="en">
<head>
<meta charset="utf-8">
<title>Thornwell Advisory – Journey Framework</title>
<link rel="stylesheet" href="https://fonts.googleapis.com/css2?family=Poppins:wght@400;500;600;700&display=swap">
<style>
:root{
  --backdrop:#bdbdbd;
  --paper:#ffffff;
  --navy:#0d2b4e;
  --tile:#0a9fd9;
  --ring:#7fd0f2;
  --line:#cfd3d6;
  --accent:#f3912a;
  --brand:#1ba0dc;
}
*{margin:0;padding:0;box-sizing:border-box}
html,body{width:1200px;height:906px;overflow:hidden;background:var(--backdrop);font-family:"Poppins",sans-serif}
.stage{position:relative;width:1200px;height:906px}
.sheet{position:absolute;left:101px;top:121px;width:996px;height:664px;background:var(--paper)}
.brand{position:absolute;left:470px;top:158px;display:flex;align-items:center;gap:14px}
.brand-dot{width:62px;height:62px;border-radius:50%;background:var(--brand)}
.brand-name{color:var(--brand);font-weight:400;font-size:27px;line-height:30px;letter-spacing:1px;text-transform:uppercase}
.headline{position:absolute;left:101px;width:996px;top:262px;text-align:center;color:var(--navy);font-weight:700;font-size:20px;line-height:26px;text-transform:uppercase}
.links{position:absolute;left:0;top:0}
.tile{position:absolute;width:104px;background:var(--tile);border-radius:3px;color:#fff;font-weight:500;font-size:16px;line-height:19px;text-align:center;display:flex;align-items:center;justify-content:center;padding-top:24px}
.tile.small{font-size:14px;line-height:17px}
.badge{position:absolute;left:50%;top:-24px;transform:translateX(-50%);width:52px;height:52px;border-radius:50%;background:var(--navy);border:2px solid var(--ring);box-shadow:0 0 0 2px #fff;display:flex;align-items:center;justify-content:center}
.badge svg{width:28px;height:28px;fill:none;stroke:#fff;stroke-width:2;stroke-linecap:round;stroke-linejoin:round}
.top{top:392px;height:75px}
.bottom{top:628px;height:81px}
.side-a{top:459px;height:79px}
.side-b{top:568px;height:83px}
.stage-label{position:absolute;width:140px;margin-left:-70px;text-align:center;color:var(--navy);font-weight:600;font-size:16px;line-height:19px;text-transform:uppercase}
</style>
</head>
<body>
<div class="stage">
  <div class="sheet"></div>

  <div class="brand">
    <div class="brand-dot"></div>
    <div class="brand-name">Thornwell<br>Advisory</div>
  </div>

  <h1 class="headline">Over thirty years we have identified that the key to being successful on<br>this journey are the following elements or components.</h1>

  <svg class="links" width="1200" height="906" viewBox="0 0 1200 906">
    <rect x="225" y="440" width="755" height="219" rx="28" fill="none" stroke="var(--line)" stroke-width="2"/>
    <g stroke="var(--accent)" stroke-width="2" stroke-dasharray="3 4">
      <line x1="347" y1="510" x2="347" y2="558"/>
      <line x1="521" y1="510" x2="521" y2="558"/>
      <line x1="687" y1="510" x2="687" y2="558"/>
      <line x1="851" y1="510" x2="851" y2="558"/>
    </g>
    <g fill="#fff" stroke="var(--accent)" stroke-width="1.5">
      <path d="M347 505l4 4-4 4-4-4z"/><path d="M347 556l4 4-4 4-4-4z"/>
      <path d="M521 505l4 4-4 4-4-4z"/><path d="M521 556l4 4-4 4-4-4z"/>
      <path d="M687 505l4 4-4 4-4-4z"/><path d="M687 556l4 4-4 4-4-4z"/>
      <path d="M851 505l4 4-4 4-4-4z"/><path d="M851 556l4 4-4 4-4-4z"/>
    </g>
    <g stroke="var(--navy)" stroke-width="1.6" fill="none">
      <path d="M418 493h34M447 488l6 5-6 5" stroke-dasharray="2 3"/>
      <path d="M589 493h32M616 488l6 5-6 5" stroke-dasharray="2 3"/>
      <path d="M744 493h22M761 488l6 5-6 5" stroke-dasharray="2 3"/>
      <path d="M418 580h34M447 575l6 5-6 5" stroke-dasharray="2 3"/>
      <path d="M589 580h32M616 575l6 5-6 5" stroke-dasharray="2 3"/>
      <path d="M739 580h27M761 575l6 5-6 5" stroke-dasharray="2 3"/>
    </g>
  </svg>

  <div class="stage-label" style="left:347px;top:485px">Get fit</div>
  <div class="stage-label" style="left:521px;top:485px">Get funded</div>
  <div class="stage-label" style="left:687px;top:485px">Get big</div>
  <div class="stage-label" style="left:851px;top:485px">Get out</div>
  <div class="stage-label" style="left:355px;top:570px">Disciplined</div>
  <div class="stage-label" style="left:521px;top:566px">Access to<br>capital</div>
  <div class="stage-label" style="left:687px;top:573px">Grow</div>
  <div class="stage-label" style="left:855px;top:566px">Exit with<br>wealth</div>

  <div class="tile top" style="left:296px"><span class="badge"><svg viewBox="0 0 28 28"><path d="M3 14s4-7 11-7 11 7 11 7-4 7-11 7S3 14 3 14z"/><circle cx="14" cy="14" r="3.5" fill="#fff"/></svg></span>Vision</div>
  <div class="tile top" style="left:465px"><span class="badge"><svg viewBox="0 0 28 28"><path d="M9 23h12l-1-5c2-3 2-8-3-12l-2 2-5 4 1 2 4-1-5 5z"/><path d="M7 25h16"/></svg></span>Strategy</div>
  <div class="tile top" style="left:633px"><span class="badge"><svg viewBox="0 0 28 28"><rect x="11" y="3" width="6" height="5"/><rect x="3" y="20" width="6" height="5"/><rect x="11" y="20" width="6" height="5"/><rect x="19" y="20" width="6" height="5"/><path d="M14 8v12M6 20v-6h16v6"/></svg></span>Structure</div>
  <div class="tile top small" style="left:797px"><span class="badge"><svg viewBox="0 0 28 28"><circle cx="14" cy="6" r="3"/><rect x="9" y="11" width="10" height="7"/><path d="M3 20l6 4h10l6-5"/></svg></span>Product &amp;<br>Services</div>

  <div class="tile bottom" style="left:296px"><span class="badge"><svg viewBox="0 0 28 28"><circle cx="11" cy="11" r="5"/><circle cx="11" cy="11" r="1.5"/><circle cx="19" cy="19" r="4"/><circle cx="19" cy="19" r="1"/></svg></span>System &amp;<br>Processes</div>
  <div class="tile bottom" style="left:465px"><span class="badge"><svg viewBox="0 0 28 28"><path d="M10 8h6l-2-4h-2zM8 24c-4 0-4-4-2-8l4-8h6l4 8c2 4 2 8-2 8z"/><path d="M13 13v8M11 15h4M11 19h4"/></svg></span>Finance</div>
  <div class="tile bottom" style="left:633px"><span class="badge"><svg viewBox="0 0 28 28"><circle cx="8" cy="8" r="4"/><path d="M8 6v4"/><path d="M4 24l8-8 4 3 8-9M20 10h4v4"/><path d="M14 24v-3M18 24v-5M22 24v-7"/></svg></span>Sales &amp;<br>Marketing</div>
  <div class="tile bottom" style="left:797px"><span class="badge"><svg viewBox="0 0 28 28"><path d="M3 12l5-4 5 3 5-3 7 4"/><path d="M7 15l5 5c1 1 2 1 3 0l6-6"/><rect x="8" y="3" width="12" height="4"/></svg></span>M&amp;A</div>

  <div class="tile side-a small" style="left:151px"><span class="badge"><svg viewBox="0 0 28 28"><circle cx="14" cy="14" r="10"/><circle cx="14" cy="14" r="5"/><path d="M14 14l6-6"/></svg></span>Performance<br>monitoring</div>
  <div class="tile side-b small" style="left:151px"><span class="badge"><svg viewBox="0 0 28 28"><path d="M4 22a10 10 0 0 1 20 0"/><path d="M14 9l6 11H8z"/><path d="M14 13v3M14 18v.5"/></svg></span>Risk Manage<br>-ment</div>
  <div class="tile side-a" style="left:945px"><span class="badge"><svg viewBox="0 0 28 28"><circle cx="14" cy="9" r="3"/><circle cx="7" cy="11" r="2.5"/><circle cx="21" cy="11" r="2.5"/><path d="M9 22v-4a5 5 0 0 1 10 0v4M3 22v-3a4 4 0 0 1 5-3M25 22v-3a4 4 0 0 0-5-3"/></svg></span>People</div>
  <div class="tile side-b" style="left:945px"><span class="badge"><svg viewBox="0 0 28 28"><circle cx="14" cy="14" r="4"/><circle cx="14" cy="4" r="2"/><circle cx="14" cy="24" r="2"/><circle cx="4" cy="14" r="2"/><circle cx="24" cy="14" r="2"/><path d="M14 6v4M14 18v4M6 14h4M18 14h4"/></svg></span>Culture</div>
</div>
</body>
</html>
```